Direct to Consumer extended service contract business with a new disruptive business model needs a

We need a customized wordpress design for a company called 'Bright Harbor Assurance'.
We provide an innovative and unique service contract protection program direct to consumers. This program provides monthly coverage for all electronics purchased in the last 4 years and all electronics the consumer purchases in the future for a low monthly fee. The overall design should communicate a sense of legitimacy, ethics, and superior customer service and support (in an industry that has a huge PR issue to overcome).
Electronics is the first product group, other product groups with different price points to launch in the future..

Target Market(s)

All purchasers of electronic goods...all demographics

Industry/Entity Type

Electronics

Font styles to use
Sans Serif

Requirements
Must have
• Customer Testimonials
Industry News
Customer ratings
Blog posts
Call to action messaging
Like the functional elements and design of veltomarket.example (need to be better)
Nice to have
• Like to see video testimonials
Social network "whats trending related to electronics or service contract industry"
Easy way to register products for warranty

```html
<!DOCTYPE html>
<html lang="en">
<head>
<meta charset="utf-8">
<title>Bright Harbor Assurance</title>
<link href="https://fonts.googleapis.com/css2?family=Roboto:wght@400;500;700&display=swap" rel="stylesheet">
<style>
:root{
  --teal:#2b7772;
  --teal-dark:#246a65;
  --red:#b31b1b;
  --beige:#ecdcc8;
  --cream:#f8ede0;
  --mist:#d3e3e3;
  --blue-rule:#9fd0df;
  --grey-text:#555;
  --footer:#c9c9c9;
  --white:#fff;
}
*{margin:0;padding:0;box-sizing:border-box}
html,body{width:823px;height:1200px;overflow:hidden;background:var(--white)}
body{position:relative;font-family:"Roboto",Arial,sans-serif;color:var(--grey-text)}
.abs{position:absolute}
.brand{left:50px;top:32px;color:var(--teal);font-weight:700;font-size:22px;line-height:22px;letter-spacing:.5px;width:190px}
.search-tab{left:591px;top:55px;width:213px;height:34px}
.search-label{left:631px;top:66px;color:var(--white);font-size:9px;display:flex;align-items:center;gap:4px}
.search-field{left:678px;top:65px;width:68px;height:11px;background:var(--white);border-radius:6px}
.nav{left:40px;top:88px;width:764px;height:26px;background:var(--red);border-radius:4px 4px 0 0;display:flex;align-items:center;padding-left:14px;font-size:12px;color:var(--white)}
.nav span{padding:0 7px}
.nav i{font-style:normal}
.strip{left:40px;top:114px;width:764px;height:11px;background:var(--teal);border-radius:0 0 3px 3px}
.hero{left:40px;top:125px;width:557px;height:217px;background:linear-gradient(100deg,#d9d6d2 0%,#a9a7a5 40%,#4d5565 70%,#2f3644 100%)}
.hero-title{left:85px;top:193px;color:var(--teal);font-size:22px;line-height:26px}
.hero-base{left:40px;top:342px;width:557px;height:22px;background:var(--beige)}
.dots{left:58px;top:347px;display:flex;gap:2px}
.dots b{width:8px;height:8px;border-radius:50%;border:1px solid #aaa;background:var(--white)}
.dots b:first-child{background:#2aa0b8;border-color:#2aa0b8}
.side{left:597px;top:125px;width:207px;height:406px;background:var(--beige)}
.side h2{position:absolute;left:11px;top:40px;color:var(--red);font-size:20px;font-weight:500}
.field{position:absolute;left:20px;width:176px;background:var(--white);font-size:7px;color:#777;padding:11px 6px}
.submit{position:absolute;left:155px;top:292px;background:var(--teal);color:var(--white);font-size:7.5px;padding:3px 6px}
.side-brand{position:absolute;left:22px;top:335px;width:170px;color:#b9b9b9;font-weight:700;font-size:22px;line-height:24px}
h3.sec{position:absolute;color:var(--teal);font-weight:400;font-size:19px}
.welcome-text{left:46px;top:415px;width:499px;font-size:9px;line-height:11.6px;text-align:justify}
.more{color:var(--teal);font-size:9px}
.band{left:40px;top:558px;width:764px;height:162px;background:var(--teal)}
.photo-frame{background:var(--teal);padding:5px}
.photo{width:100%;height:100%}
.quote{color:var(--white);font-size:9px;line-height:11.6px;width:222px}
.quote strong{display:block;font-size:12.5px;margin-bottom:8px}
.news{left:40px;top:734px;width:386px;height:256px;background:var(--cream)}
.blog{left:434px;top:734px;width:370px;height:256px;background:var(--mist)}
.item-thumb{position:absolute;left:11px;width:60px;height:52px;background:#7c7c7c}
.item-text{position:absolute;font-size:11px;line-height:13.6px;color:#666}
.rule{position:absolute;height:3px}
.footer{left:42px;top:1019px;width:762px;height:181px;background:var(--footer);border-top:2px solid #d8d8d8}
.f-brand{position:absolute;left:22px;top:36px;width:150px;color:#7a7a7a;font-weight:700;font-size:18px;line-height:20px}
.f-col{position:absolute;font-size:7px;line-height:9.5px;color:#666}
.vline{position:absolute;top:20px;width:1px;height:110px;background:#b3b3b3}
.social{position:absolute;left:361px;top:63px;display:flex;align-items:center;gap:3px;font-size:13px;color:#666}
.social b{width:19px;height:19px;border-radius:50%;background:#555;display:inline-block}
.social span{margin-right:11px}
.nl-label{position:absolute;left:564px;top:30px;font-size:10.5px;color:#666}
.nl-field{position:absolute;left:560px;top:46px;width:160px;height:24px;background:var(--white);border:2px solid #bbb}
.nl-submit{position:absolute;left:690px;top:78px;background:var(--white);border:1px solid #999;font-size:7px;padding:2px 5px;color:#333}
.copy{position:absolute;left:298px;top:163px;font-size:6.5px;color:#666}
</style>
</head>
<body>

<div class="abs brand">Bright Harbor<br>Assurance</div>

<svg class="abs search-tab" viewBox="0 0 213 34" aria-hidden="true">
  <path d="M0 34 C14 34 18 12 26 4 Q30 0 38 0 H180 Q192 0 198 10 L213 34 Z" fill="var(--teal)"/>
</svg>
<div class="abs search-label">
  <svg width="11" height="11" viewBox="0 0 11 11"><circle cx="6.5" cy="4.5" r="3.3" fill="none" stroke="#fff" stroke-width="1.5"/><line x1="4" y1="7" x2="1" y2="10" stroke="#fff" stroke-width="1.8"/></svg>
  SEARCH
</div>
<div class="abs search-field"></div>

<nav class="abs nav">
  <span>Home</span><i>|</i><span>About us</span><i>|</i><span>Our Services</span><i>|</i><span>Industry News</span><i>|</i><span>Customer ratings</span><i>|</i><span>Bolg</span><i>|</i><span>Contacu us</span>
</nav>
<div class="abs strip"></div>

<div class="abs hero" role="img" aria-label="Photo of two smiling businessmen in suits at a laptop"></div>
<div class="abs hero-title">Unique service contract<br>protection program</div>
<div class="abs hero-base"></div>
<div class="abs dots"><b></b><b></b><b></b><b></b><b></b><b></b></div>

<aside class="abs side">
  <h2>Contact us</h2>
  <div class="field" style="top:73px;height:28px">Your name</div>
  <div class="field" style="top:107px;height:28px">Phone Number</div>
  <div class="field" style="top:145px;height:28px">Email address</div>
  <div class="field" style="top:184px;height:104px">Your Message</div>
  <div class="submit">Submit</div>
  <div class="side-brand">Bright Harbor<br>Assurance</div>
</aside>

<h3 class="sec" style="left:45px;top:383px">Welcome to Bright Harbor Assurance</h3>
<p class="abs welcome-text">We provide an innovative and unique service contract protection program direct to consumers. This program provides monthly coverage for all electronics purchased in the last 4 years and all electronics the consumer purchases in the future for a low monthly fee. The overall design should communicate a sense of legitimacy, ethics, and superior customer service and support (in an industry that has a huge PR issue to overcome).<br>Electronics is the first product group, other product groups with different price points to launch in the future..</p>
<div class="abs more" style="left:444px;top:481px">Read More</div>

<h3 class="sec" style="left:46px;top:512px">Customer Testimonials</h3>
<div class="abs band"></div>
<div class="abs photo-frame" style="left:66px;top:541px;width:107px;height:141px">
  <div class="photo" role="img" aria-label="Portrait photo of a smiling young man in a blue shirt" style="background:linear-gradient(180deg,#e8e8e6,#9db4cf)"></div>
</div>
<div class="abs quote" style="left:181px;top:571px"><strong>Owen Castell</strong>Bright Harbor Help me To Give high protection Bright Harbor Help me To Give high protection Bright Harbor Help me To Give high protection Bright Harbor Help me To Give high protection Bright Harbor Help me To Give high protection Bright Harbor Help me To Give high protection Bright Harbor Help me To Give high protection Bright Harbor Help me To Give high protection</div>
<div class="abs photo-frame" style="left:439px;top:541px;width:106px;height:130px">
  <div class="photo" role="img" aria-label="Portrait photo of a smiling woman with dark hair" style="background:linear-gradient(180deg,#f1efed,#d8c4b4)"></div>
</div>
<div class="abs quote" style="left:564px;top:571px"><strong>Lena Marsh</strong>Bright Harbor Help me To Give high protection Bright Harbor Help me To Give high protection Bright Harbor Help me To Give high protection Bright Harbor Help me To Give high protection Bright Harbor Help me To Give high protection Bright Harbor Help me To Give high protection Bright Harbor Help me To Give high protection Bright Harbor Help me To Give high protection</div>

<section class="abs news">
  <h3 class="sec" style="left:15px;top:4px">Industry News</h3>
  <div class="item-thumb" style="top:42px"></div>
  <div class="item-text" style="left:78px;top:44px;width:275px">Our Bright Harbor News Our Bright Harbor News Our Bright Harbor News Our Bright Harbor News Our Bright Harbor News</div>
  <div class="abs more" style="left:288px;top:85px">Read More..</div>
  <div class="rule" style="left:16px;top:102px;width:331px;background:#e3d5c3"></div>
  <div class="item-thumb" style="top:112px"></div>
  <div class="item-text" style="left:78px;top:114px;width:275px">Our Bright Harbor News Our Bright Harbor News Our Bright Harbor News Our Bright Harbor News Our Bright Harbor News</div>
  <div class="abs more" style="left:288px;top:155px">Read More..</div>
  <div class="rule" style="left:16px;top:172px;width:331px;background:#e3d5c3"></div>
  <div class="item-thumb" style="top:182px"></div>
  <div class="item-text" style="left:78px;top:184px;width:275px">Our Bright Harbor News Our Bright Harbor News Our Bright Harbor News Our Bright Harbor News Our Bright Harbor News</div>
  <div class="abs more" style="left:288px;top:225px">Read More..</div>
  <div class="rule" style="left:16px;top:242px;width:331px;background:#e3d5c3"></div>
</section>

<section class="abs blog">
  <h3 class="sec" style="left:12px;top:4px">Blog posts</h3>
  <div class="item-text" style="left:25px;top:32px;width:312px">Blog Posts Blog Posts Blog Posts Blog Posts Blog Posts Blog Posts Blog Posts Blog Posts Blog Posts Blog Posts Blog Posts Blog Posts Blog Posts</div>
  <div class="abs more" style="left:275px;top:75px">Read More..</div>
  <div class="rule" style="left:19px;top:86px;width:330px;background:var(--blue-rule)"></div>
  <div class="item-text" style="left:25px;top:100px;width:312px">Blog Posts Blog Posts Blog Posts Blog Posts Blog Posts Blog Posts Blog Posts Blog Posts Blog Posts Blog Posts Blog Posts Blog Posts Blog Posts</div>
  <div class="abs more" style="left:275px;top:143px">Read More..</div>
  <div class="rule" style="left:19px;top:154px;width:330px;background:var(--blue-rule)"></div>
  <div class="item-text" style="left:25px;top:167px;width:312px">Blog Posts Blog Posts Blog Posts Blog Posts Blog Posts Blog Posts Blog Posts Blog Posts Blog Posts Blog Posts Blog Posts Blog Posts Blog Posts</div>
  <div class="abs more" style="left:275px;top:210px">Read More..</div>
  <div class="rule" style="left:19px;top:221px;width:330px;background:var(--blue-rule)"></div>
</section>

<footer class="abs footer">
  <div class="f-brand">Bright Harbor<br>Assurance</div>
  <div class="vline" style="left:191px"></div>
  <div class="f-col" style="left:206px;top:30px">Home<br>About<br>Contact<br>Media</div>
  <div class="f-col" style="left:266px;top:29px">Our Services<br>Industry News<br>Customer Rating<br>Blog</div>
  <div class="vline" style="left:340px"></div>
  <div class="social"><span>Social</span><b></b><b></b><b></b><b></b><b></b></div>
  <div class="vline" style="left:538px"></div>
  <div class="nl-label">Subscribe to our newsletter</div>
  <div class="nl-field"></div>
  <div class="nl-submit">Submit</div>
  <div class="copy">Copyright 2014 Bright Harbor Assurance</div>
</footer>

</body>
</html>
```